Update Pulp Pantry menu board to appear Fresh and modern

I need a menu board design that is not cluttered, easy to read, playful and the style of healthy and fresh for a juice bar. I will be editing the details of the items, so basically the design is all I need. I prefer the files to be in Microsoft Publisher as I am most familiar, but I have illustrator as well, but not as advanced on that. The size should be 36"x36". I will create 3 seperate boards from the one design.

Target Market(s)

health concious people, active lifestyle people

Font styles to use
Serif

Colors

Designer to choose colors to be used in the design.

Requirements
Must have
• Not cluttered
• Modern feel
Nice to have
• i like the style of the
• "cold pressed juice" part of my attached juice bottle label

```html
<!DOCTYPE html>
<html lang="en">
<head>
<meta charset="utf-8">
<title>Pulp Pantry Menu Board</title>
<link rel="stylesheet" href="https://fonts.googleapis.com/css2?family=Alfa+Slab+One&family=Open+Sans:wght@300;600;700&family=Saira+Condensed:wght@700&family=Oswald:wght@400&display=swap">
<style>
:root{
  --plum:#442033;
  --plum-edge:#7d6466;
  --wood-light:#dcb994;
  --wood-dark:#c39a70;
  --orange:#f7931e;
  --green:#6cbf3a;
  --pink:#ec3e94;
  --copy:#f3b56b;
  --label-bg:#5b5858;
  --label-text:#ececec;
  --price:#ffffff;
  --brand-ink:#f26b21;
  --brand-dot:#f26b21;
  --leaf-a:#5fb83a;
  --leaf-b:#1f7a2a;
}
*{margin:0;padding:0;box-sizing:border-box}
html,body{width:1200px;height:1200px;overflow:hidden}
body{position:relative;background:var(--wood-dark);font-family:"Open Sans",sans-serif}
.wood{position:absolute;left:0;width:1200px;background:linear-gradient(160deg,var(--wood-light) 0%,var(--wood-dark) 45%,var(--wood-light) 70%,var(--wood-dark) 100%)}
.wood--top{top:0;height:260px}
.wood--bottom{top:1160px;height:40px}
.board-shape{position:absolute;left:0;top:0;width:1200px;height:1200px}
.foliage{position:absolute;top:22px;width:324px;height:180px;border-radius:50%;background:radial-gradient(ellipse at center,var(--leaf-a) 0%,var(--leaf-b) 55%,rgba(31,122,42,0) 72%)}
.foliage--left{left:41px}
.foliage--right{left:837px}
.brand__dot{position:absolute;left:365px;top:41px;width:156px;height:156px;border-radius:50%;background:var(--brand-dot)}
.brand__name{position:absolute;left:530px;top:42px;font-family:"Alfa Slab One",serif;font-size:64px;line-height:72px;color:var(--brand-ink);text-transform:uppercase;white-space:nowrap}
.col{position:absolute;top:0;width:330px;height:1200px}
.col--cold{left:110px;color:var(--orange)}
.col--warm{left:456px;color:var(--green)}
.col--breakfast{left:802px;color:var(--pink)}
.section-title{position:absolute;left:0;top:222px;white-space:nowrap}
.section-title__light{display:block;font-family:"Open Sans",sans-serif;font-weight:300;font-size:64px;letter-spacing:3px;line-height:64px}
.section-title__heavy{display:block;font-family:"Alfa Slab One",serif;font-size:58px;line-height:56px;letter-spacing:1px}
.section-title--stacked{top:226px}
.section-title--stacked .section-title__heavy{line-height:54px}
.divider{position:absolute;top:361px;width:1.5px;height:762px;background:var(--plum-edge)}
.divider--cold{left:-12.5px}
.divider--warm,.divider--breakfast{left:-12px}
.item{position:absolute;left:0;width:340px}
.item__name{font-family:"Saira Condensed",sans-serif;font-weight:700;font-size:30px;line-height:30px;text-transform:uppercase;white-space:nowrap}
.item__desc{margin-top:2px;font-weight:700;font-size:13px;line-height:16.4px;color:var(--copy);text-transform:uppercase;white-space:nowrap}
.item__note{font-weight:600;font-size:8.5px;line-height:11px;color:var(--copy);white-space:nowrap}
.sizes{display:flex;column-gap:11px;margin-top:3px}
.size{width:60px;text-align:center}
.size__label{display:block;height:18px;background:var(--label-bg);color:var(--label-text);font-size:12.5px;font-weight:600;line-height:18px}
.size__price{display:block;font-family:"Oswald",sans-serif;font-size:32px;line-height:36px;color:var(--price);transform:scaleX(0.82)}
.served{position:absolute;left:0;top:1086px;font-family:"Alfa Slab One",serif;font-size:26px;line-height:32px;letter-spacing:3px;color:var(--pink);white-space:nowrap}
</style>
</head>
<body>
<div class="wood wood--top"></div>
<div class="wood wood--bottom"></div>
<svg class="board-shape" viewBox="0 0 1200 1200" aria-hidden="true">
  <path d="M0,196 Q600,-14 1200,196 L1200,246 Q600,36 0,246 Z" fill="#a08a80" opacity="0.55"/>
  <path d="M0,246 Q600,36 1200,246 L1200,1160 L0,1160 Z" fill="#442033"/>
  <rect x="0" y="1160" width="1200" height="9" fill="#8a7d78"/>
</svg>
<div class="foliage foliage--left" role="img" aria-label="Green leafy sprigs"></div>
<div class="foliage foliage--right" role="img" aria-label="Green leafy sprigs"></div>

<header class="brand">
  <div class="brand__dot"></div>
  <div class="brand__name">Pulp<br>Pantry</div>
</header>

<section class="col col--cold">
  <h2 class="section-title"><span class="section-title__light">COLD</span><span class="section-title__heavy">WRAPS</span></h2>
  <div class="divider divider--cold"></div>
  <article class="item" style="top:359px">
    <h3 class="item__name">BLT Ranch Wrap</h3>
    <p class="item__desc">Roasted red pepper hummus,<br>kalamata olives, spring mix,<br>tomato on a wheat tortilla</p>
    <p class="item__note">Add Chicken to a Sm/Reg 1.50&nbsp; Lrg 2.50</p>
    <div class="sizes"><div class="size"><span class="size__label">Small</span><span class="size__price">5</span></div><div class="size"><span class="size__label">Regular</span><span class="size__price">6.75</span></div><div class="size"><span class="size__label">Large</span><span class="size__price">8.75</span></div></div>
  </article>
  <article class="item" style="top:527px">
    <h3 class="item__name">Pesto Wrap</h3>
    <p class="item__desc">Grilled chicken breast, spring<br>mix, tomatoes, sun dried<br>tomato pesto</p>
    <div class="sizes"><div class="size"><span class="size__label">Small</span><span class="size__price">5</span></div><div class="size"><span class="size__label">Regular</span><span class="size__price">6.50</span></div><div class="size"><span class="size__label">Large</span><span class="size__price">8.25</span></div></div>
  </article>
  <article class="item" style="top:684px">
    <h3 class="item__name">Chicken Caesar</h3>
    <p class="item__desc">Grilled chicken breast, romaine<br>lettuce, parmesan, caesar<br>dressing</p>
    <div class="sizes"><div class="size"><span class="size__label">Small</span><span class="size__price">5</span></div><div class="size"><span class="size__label">Regular</span><span class="size__price">6.50</span></div><div class="size"><span class="size__label">Large</span><span class="size__price">8.25</span></div></div>
  </article>
  <article class="item" style="top:839px">
    <h3 class="item__name">Buffalo Chicken</h3>
    <p class="item__desc">Lightly breaded buffalo chicken,<br>mixed greens, tomato, ranch</p>
    <div class="sizes"><div class="size"><span class="size__label">Small</span><span class="size__price">5</span></div><div class="size"><span class="size__label">Regular</span><span class="size__price">6.50</span></div><div class="size"><span class="size__label">Large</span><span class="size__price">8.25</span></div></div>
  </article>
  <article class="item" style="top:977px">
    <h3 class="item__name">Greek Wrap</h3>
    <p class="item__desc">Roasted red pepper hummus,<br>kalamata olives, spring mix,<br>tomato on a wheat tortilla</p>
    <p class="item__note">Add Chicken to a Small 1.50 or Large 2.50</p>
    <div class="sizes"><div class="size"><span class="size__label">Regular</span><span class="size__price">4.75</span></div><div class="size"><span class="size__label">Large</span><span class="size__price">7.50</span></div></div>
  </article>
</section>

<section class="col col--warm">
  <h2 class="section-title"><span class="section-title__light">WARM</span><span class="section-title__heavy">WRAPS</span></h2>
  <div class="divider divider--warm"></div>
  <article class="item" style="top:359px">
    <h3 class="item__name">Cheese Steak Wrap</h3>
    <p class="item__desc">Thinly sliced beef, onions,<br>peppers and cheddar jack cheese</p>
    <div class="sizes"><div class="size"><span class="size__label">Regular</span><span class="size__price">7.50</span></div><div class="size"><span class="size__label">Large</span><span class="size__price">15</span></div></div>
  </article>
  <article class="item" style="top:499px">
    <h3 class="item__name">BBQ Chicken Wrap</h3>
    <p class="item__desc">Chicken breast, bacon, onion<br>strings, BBQ sauce and cheddar<br>jack cheese</p>
    <div class="sizes"><div class="size"><span class="size__label">Regular</span><span class="size__price">8</span></div><div class="size"><span class="size__label">Large</span><span class="size__price">15.50</span></div></div>
  </article>
  <article class="item" style="top:654px">
    <h3 class="item__name">Philly Chicken Wrap</h3>
    <p class="item__desc">Chicken breast, onions, peppers<br>and cheddar jack cheese</p>
    <div class="sizes"><div class="size"><span class="size__label">Regular</span><span class="size__price">6.75</span></div><div class="size"><span class="size__label">Large</span><span class="size__price">12.50</span></div></div>
  </article>
  <article class="item" style="top:793px">
    <h3 class="item__name">Venetian Chicken Wrap</h3>
    <p class="item__desc">Grilled chicken breast, roasted<br>red peppers, tomato, cheddar<br>jack cheese and sun dried<br>tomato pesto</p>
    <div class="sizes"><div class="size"><span class="size__label">Regular</span><span class="size__price">6.75</span></div><div class="size"><span class="size__label">Large</span><span class="size__price">12.50</span></div></div>
  </article>
  <article class="item" style="top:965px">
    <h3 class="item__name">Chicken &amp; Broccoli</h3>
    <p class="item__desc">Grilled chicken breast, steamed<br>broccoli and cheddar jack<br>cheese</p>
    <div class="sizes"><div class="size"><span class="size__label">Regular</span><span class="size__price">6.75</span></div><div class="size"><span class="size__label">Large</span><span class="size__price">12.50</span></div></div>
  </article>
</section>

<section class="col col--breakfast">
  <h2 class="section-title section-title--stacked"><span class="section-title__heavy">BREAK</span><span class="section-title__heavy">FAST</span></h2>
  <div class="divider divider--breakfast"></div>
  <article class="item" style="top:359px">
    <h3 class="item__name">Bacon Burrito</h3>
    <p class="item__desc">Bacon, scrambled eggs,<br>potato, cheese with green chili</p>
    <div class="sizes"><div class="size"><span class="size__label">Regular</span><span class="size__price">5.50</span></div><div class="size"><span class="size__label">Large</span><span class="size__price">10</span></div></div>
  </article>
  <article class="item" style="top:499px">
    <h3 class="item__name">Sausage Burrito</h3>
    <p class="item__desc">Sausage, scrambled eggs,<br>potato, cheese, green chili</p>
    <div class="sizes"><div class="size"><span class="size__label">Regular</span><span class="size__price">5.50</span></div><div class="size"><span class="size__label">Large</span><span class="size__price">10</span></div></div>
  </article>
  <article class="item" style="top:638px">
    <h3 class="item__name">Meat &amp; Potatoes Burrito</h3>
    <p class="item__desc">Philly beef, scrambled eggs,<br>potato, cheese, green chili</p>
    <div class="sizes"><div class="size"><span class="size__label">Regular</span><span class="size__price">7.50</span></div><div class="size"><span class="size__label">Large</span><span class="size__price">15</span></div></div>
  </article>
  <article class="item" style="top:777px">
    <h3 class="item__name">Bean Breakfast Burrito</h3>
    <p class="item__desc">Scrambled eggs, refried beans,<br>green chili, potato, cheese</p>
    <div class="sizes"><div class="size"><span class="size__label">Regular</span><span class="size__price">5.50</span></div><div class="size"><span class="size__label">Large</span><span class="size__price">10</span></div></div>
  </article>
  <article class="item" style="top:916px">
    <h3 class="item__name">Veggie Omelet Burrito</h3>
    <p class="item__desc">Scrambled eggs, spinach, roasted<br>red peppers, tomato, cheese,<br>green chili on a wheat tortilla</p>
    <div class="sizes"><div class="size"><span class="size__label">Regular</span><span class="size__price">5.50</span></div><div class="size"><span class="size__label">Large</span><span class="size__price">10</span></div></div>
  </article>
  <p class="served">SERVED ALL DAY</p>
</section>
</body>
</html>
```